Rodent & Wildlife Services from Harborline Termite & Pest Control

I want to show all of the steps in our Rodent/Wildlife Treatment plan:
Inspection- a Harborline wildlife specialist will do a thorough inspection of the Attic and exterior of your home. We will provide you will a detailed Report and Pictures of any infestations found and any areas found to be contaminated. We will also identify any current or potential entry points into the home.
Trapping/Removal- we will create a plan to trap any infestation and remove them- each situation is different and may require a variety of techniques.
Decontamination- animals will leave behind urine, feces, and oils that can potentially contain a variety of bacterias and deseases. We will include in the treatment plan a process to remove and clean up these areas.
Entry Prevention- it is very important to seal up any potential entry points after the infestation has been eliminated. This will help prevent any future infestations into the structure.
Ongoing Protection- Harborline will set up a Rodent baiting program to reduce any surrounding populations.

my thought is to have a picture of each Step and then description (bullet points) about that step

Target Market(s)

Residential

Industry/Entity Type

Pest Control

Font styles to use
Other font styles liked:
• Times Roman

Colors
0455a3
ec1f27

Requirements
Must have
• Professional, concise look.

```html
<!DOCTYPE html>
<html lang="en">
<head>
<meta charset="utf-8">
<title>Harborline Rodent &amp; Wildlife Services Brochure</title>
<link rel="stylesheet" href="https://fonts.googleapis.com/css2?family=Tinos:ital,wght@0,400;0,700;1,400&display=swap">
<style>
  :root{
    --brand-blue:#0455a3;
    --brand-red:#ec1f27;
    --ink:#1f2229;
    --paper:#ffffff;
    --rule:#c9d3e0;
  }
  *{box-sizing:border-box;margin:0;padding:0}
  html,body{width:1200px;height:3389px;overflow:hidden;background:var(--paper)}
  body{position:relative;font-family:"Tinos","Times New Roman",serif;color:var(--ink)}
  .sheet{
    position:absolute;top:0;left:0;width:3389px;height:1200px;
    transform-origin:0 0;transform:translate(1200px,0) rotate(90deg);
    background:var(--paper);display:flex;
  }
  .edge-band{position:absolute;left:0;right:0;bottom:0;height:92px;background:var(--brand-red)}
  .edge-cap{position:absolute;left:0;top:0;bottom:0;width:34px;background:var(--brand-red)}
  .panel{position:relative;height:1200px;padding:70px 70px 150px}
  .panel + .panel{border-left:2px solid var(--rule)}
  .panel--steps{width:1130px;padding-left:90px}
  .panel--plan{width:1130px}
  .panel--cover{width:1129px}

  .photo-column{position:absolute;left:90px;top:0;width:170px;display:flex;flex-direction:column;gap:14px;padding-top:12px}
  .photo{height:180px;border:3px solid var(--paper);box-shadow:0 0 0 1px #bbb}
  .photo--attic-rodent{background:linear-gradient(135deg,#b89a6a,#e2d2b0)}
  .photo--insulation{background:linear-gradient(135deg,#2e3340,#6c7382)}
  .photo--crawlspace{background:linear-gradient(135deg,#8e8f8c,#d4d2cc)}

  .header-band{position:absolute;top:0;left:290px;right:140px;height:86px;background:var(--brand-blue)}
  .brand{display:flex;align-items:center;gap:16px}
  .brand-mark{width:34px;height:34px;background:var(--brand-red)}
  .brand-name{font-weight:700;font-size:64px;color:var(--brand-red);line-height:1}
  .brand-tagline{font-weight:700;font-size:24px;color:var(--brand-blue);letter-spacing:1px;margin-top:6px}
  .panel--steps .brand-block{position:absolute;left:300px;top:110px}

  .steps-copy{position:absolute;left:300px;right:80px;top:300px}
  h2.step-title{font-size:30px;color:var(--brand-blue);margin:0 0 10px}
  ul.step-points{list-style:none;margin-bottom:26px}
  ul.step-points li{font-size:22px;line-height:1.45;padding-left:24px;position:relative;margin-bottom:4px}
  ul.step-points li::before{content:"";position:absolute;left:2px;top:11px;width:9px;height:9px;background:var(--brand-red)}

  h1.plan-title{font-size:40px;color:var(--brand-blue);text-align:center;margin:10px 0 30px}
  .plan-intro{font-size:22px;line-height:1.5;margin-bottom:26px;font-style:italic}

  .cover-contact{position:absolute;left:180px;top:180px;right:200px}
  .cover-contact h3{font-size:28px;color:var(--brand-blue);margin-bottom:14px}
  .cover-contact p{font-size:22px;line-height:1.6}
  .panel--cover .brand-block{position:absolute;left:430px;top:820px;text-align:center}
  .panel--cover .brand{justify-content:center}
</style>
</head>
<body>
<div class="sheet">
  <div class="edge-cap"></div>

  <section class="panel panel--steps">
    <div class="photo-column">
      <div class="photo photo--attic-rodent" role="img" aria-label="Photo of a rodent found during an attic inspection"></div>
      <div class="photo photo--insulation" role="img" aria-label="Photo of contaminated attic insulation"></div>
      <div class="photo photo--crawlspace" role="img" aria-label="Photo of a sealed exterior entry point"></div>
    </div>
    <div class="header-band"></div>
    <div class="brand-block">
      <div class="brand"><span class="brand-mark"></span><span class="brand-name">Harborline</span></div>
      <div class="brand-tagline">TERMITE &amp; PEST CONTROL</div>
    </div>
    <div class="steps-copy">
      <h2 class="step-title">Inspection</h2>
      <ul class="step-points">
        <li>A Harborline wildlife specialist performs a thorough inspection of your attic and home exterior.</li>
        <li>You receive a detailed report with pictures of any infestation and contaminated areas.</li>
        <li>Current and potential entry points into the home are identified.</li>
      </ul>
      <h2 class="step-title">Trapping / Removal</h2>
      <ul class="step-points">
        <li>We create a plan to trap and remove any infestation.</li>
        <li>Every situation is different and may require a variety of techniques.</li>
      </ul>
    </div>
  </section>

  <section class="panel panel--plan">
    <h1 class="plan-title">Rodent &amp; Wildlife Services</h1>
    <p class="plan-intro">Our complete treatment plan protects your home from the attic to the foundation, one step at a time.</p>
    <h2 class="step-title">Decontamination</h2>
    <ul class="step-points">
      <li>Animals leave behind urine, feces and oils that may carry bacteria and diseases.</li>
      <li>Your treatment plan includes removal and clean-up of all affected areas.</li>
    </ul>
    <h2 class="step-title">Entry Prevention</h2>
    <ul class="step-points">
      <li>Potential entry points are sealed once the infestation has been eliminated.</li>
      <li>Sealing helps prevent future infestations into the structure.</li>
    </ul>
    <h2 class="step-title">Ongoing Protection</h2>
    <ul class="step-points">
      <li>Harborline sets up a rodent baiting program around your property.</li>
      <li>Baiting reduces surrounding populations and keeps your home protected.</li>
    </ul>
  </section>

  <section class="panel panel--cover">
    <div class="cover-contact">
      <h3>Schedule Your Inspection</h3>
      <p>Harborline Termite &amp; Pest Control</p>
      <p>1840 Bayview Road, Suite 3</p>
      <p>Harbor City, ST 00000</p>
      <p>(555) 014-2290</p>
      <p>harborlinepest.example</p>
    </div>
    <div class="brand-block">
      <div class="brand"><span class="brand-mark"></span><span class="brand-name">Harborline</span></div>
      <div class="brand-tagline">TERMITE &amp; PEST CONTROL</div>
    </div>
  </section>

  <div class="edge-band"></div>
</div>
</body>
</html>
```